Business Card & Email Signature Design || Upmarket + Luxury

Riverlume Honey, a New Zealand Manuka Honey company needs a Business Card & Email Signature design.

Our logo's are attached in Gold & Black versions, feel free to be creative with how you use the logo and it's patterns in your design.

Style:
- Looking for an Elegant, Luxurious, Upmarket feel.
- Black/Matte Black Card, Gold Foil, UV Embossing

Information to Add:

- Logo
- Company Name: Riverlume Honey
- Name: Mattias Brovell
- Title: Creative Director
- Phone: +64 2919 58 617
- Email: mattias@riverlumehoney.example
- Website: www.riverlumehoney.example

- Socials: ***For email Signature Only***
- Facebook: https://www.facebook.com/riverlumehoney/
- Instagram: https://www.instagram.com/riverlumehoney/

Target Market(s)

Asia/Europe Luxury, Upmarket

Contact Information for Business Card

- Logo
- Name: Mattias Brovell
- Phone: +64 2919 58 617

Font styles to use
Other font styles liked:
• Champagne & Limousines (Attached)

Requirements
Must have
• Business Card & Email Signature Design.

Looking for a Sleek, Luxury, Upmarket Design.

```html
<!DOCTYPE html>
<html lang="en">
<head>
<meta charset="utf-8">
<title>Riverlume Honey – Business Card &amp; Email Signature</title>
<link rel="stylesheet" href="https://fonts.googleapis.com/css2?family=Michroma&family=Quicksand:wght@300;400;500;600&display=swap">
<style>
  :root {
    --board: #e4e2dc;
    --label-gold: #c4a15a;
    --card-charcoal: #2b2b2b;
    --band-charcoal: #262626;
    --card-black: #050505;
    --sig-charcoal: #2a2a2a;
    --cream: #efe7d2;
    --pill-cream: #f4ecd4;
    --icon-green: #7a9a1e;
    --icon-blue: #1d6fb8;
    --icon-yellow: #d9a520;
    --icon-plum: #8a3c5c;
    --social-blue: #1d5fa8;
  }
  html, body {
    margin: 0;
    width: 1200px;
    height: 1200px;
    overflow: hidden;
    background: var(--board);
  }
  .board {
    position: relative;
    width: 1200px;
    height: 1200px;
    background: var(--board);
    font-family: "Quicksand", sans-serif;
  }
  .version-tag, .section-label {
    position: absolute;
    margin: 0;
    font-family: "Michroma", sans-serif;
    color: var(--label-gold);
    font-weight: 400;
  }
  .version-tag { top: 24px; right: 40px; font-size: 15px; letter-spacing: 2px; }
  .section-label {
    left: 0; width: 1200px; text-align: center;
    font-size: 15px; letter-spacing: 5px;
  }
  .label-card { top: 105px; }
  .label-signature { top: 656px; }
  .card-front, .card-back, .email-signature { position: absolute; display: block; }
  .card-front { left: 27px; top: 172px; width: 569px; height: 325px; }
  .card-back { left: 604px; top: 172px; width: 567px; height: 325px; }
  .email-signature {
    left: 156px; top: 709px; width: 830px; height: 357px;
    box-shadow: 0 1px 4px rgba(0,0,0,.18);
  }
  .name-light { font-weight: 300; }
  .name-strong { font-weight: 600; }
  .job-title { font-style: italic; font-weight: 400; }
  .contact-line { font-weight: 400; }
  .brand-name { font-weight: 500; letter-spacing: 2px; }
  .social-heading { font-weight: 600; }
  .social-handle { font-weight: 500; }
</style>
</head>
<body>
<main class="board">
  <p class="version-tag">V2</p>
  <h2 class="section-label label-card">BUSINESS CARD</h2>

  <!-- Business card, front -->
  <svg class="card-front" viewBox="0 0 521 298" xmlns="http://www.w3.org/2000/svg">
    <defs>
      <linearGradient id="gold-front" x1="0" y1="0" x2="1" y2="1">
        <stop offset="0" stop-color="#b98a3e"/>
        <stop offset="0.5" stop-color="#f3dc8c"/>
        <stop offset="1" stop-color="#c79a4a"/>
      </linearGradient>
      <linearGradient id="honeycomb-front" x1="0" y1="0" x2="1" y2="0">
        <stop offset="0" stop-color="#2e2e2e"/>
        <stop offset="1" stop-color="#484848"/>
      </linearGradient>
    </defs>
    <rect class="card-base" width="521" height="298" fill="var(--card-charcoal)"/>
    <rect class="honeycomb-texture" x="205" y="0" width="316" height="66" fill="url(#honeycomb-front)" role="img" aria-label="Embossed honeycomb texture"/>
    <rect class="honeycomb-texture" x="205" y="232" width="316" height="66" fill="url(#honeycomb-front)" role="img" aria-label="Embossed honeycomb texture"/>
    <circle class="sweep-arc" cx="10" cy="150" r="240" fill="none" stroke="url(#gold-front)" stroke-width="2"/>
    <rect class="info-band" x="180" y="66" width="341" height="166" fill="var(--band-charcoal)"/>
    <line x1="180" y1="66" x2="521" y2="66" stroke="url(#gold-front)" stroke-width="1.5"/>
    <line x1="180" y1="232" x2="521" y2="232" stroke="url(#gold-front)" stroke-width="1.5"/>
    <circle class="orbit-ring" cx="98" cy="142" r="90" fill="var(--card-charcoal)" stroke="url(#gold-front)" stroke-width="1.6"/>
    <circle class="brand-ring" cx="98" cy="142" r="62" fill="none" stroke="url(#gold-front)" stroke-width="1.4"/>
    <text class="brand-name" x="98" y="139" text-anchor="middle" font-size="11" fill="#d9b866">RIVERLUME</text>
    <text class="brand-name" x="98" y="154" text-anchor="middle" font-size="11" fill="#d9b866">HONEY</text>

    <text x="232" y="113" font-size="22" fill="url(#gold-front)"><tspan class="name-light">MATTIAS </tspan><tspan class="name-strong">BROVELL</tspan></text>
    <text class="job-title" x="237" y="133" font-size="14" fill="#d3ad5c">Creative Director</text>
    <line x1="210" y1="138" x2="362" y2="138" stroke="url(#gold-front)" stroke-width="1"/>
    <circle cx="362" cy="138" r="2.2" fill="#d9b866"/>

    <circle cx="212" cy="174" r="9" fill="var(--icon-green)" stroke="#f0e3b0" stroke-width="1"/>
    <path d="M208.5 170.5c.6-.6 1.4-.6 1.9 0l1 1.2c.4.5.3 1-.1 1.4l-.6.5c.5 1 1.2 1.7 2.2 2.2l.5-.6c.4-.4.9-.5 1.4-.1l1.2 1c.6.5.6 1.3 0 1.9-1.5 1.5-4 .8-5.9-1.1s-2.6-4.4-1.6-6.4z" fill="#fff"/>
    <text class="contact-line" x="236" y="182" font-size="17" fill="var(--cream)">+64 2919 58 617</text>

    <circle cx="201" cy="200" r="9" fill="var(--icon-blue)" stroke="#f0e3b0" stroke-width="1"/>
    <rect x="196" y="196.5" width="10" height="7" fill="none" stroke="#fff" stroke-width="1"/>
    <path d="M196 197l5 3.5 5-3.5" fill="none" stroke="#fff" stroke-width="1"/>
    <text class="contact-line" x="232" y="206" font-size="14" fill="var(--cream)">mattias@riverlumehoney.example</text>
  </svg>

  <!-- Business card, back -->
  <svg class="card-back" viewBox="0 0 519 298" xmlns="http://www.w3.org/2000/svg">
    <defs>
      <linearGradient id="gold-back" x1="0" y1="0" x2="1" y2="1">
        <stop offset="0" stop-color="#b98a3e"/>
        <stop offset="0.5" stop-color="#f3dc8c"/>
        <stop offset="1" stop-color="#c79a4a"/>
      </linearGradient>
    </defs>
    <rect class="card-base" width="519" height="298" fill="var(--card-black)"/>
    <text class="brand-name" x="259.5" y="170" text-anchor="middle" font-size="31" letter-spacing="4" fill="#dcbb6a">RIVERLUME HONEY</text>
    <circle class="base-arc" cx="259.5" cy="362" r="152" fill="none" stroke="url(#gold-back)" stroke-width="2.5"/>
    <circle class="base-arc" cx="259.5" cy="362" r="86" fill="none" stroke="url(#gold-back)" stroke-width="2.5"/>
  </svg>

  <h2 class="section-label label-signature">EMAIL SIGNATURE</h2>

  <!-- Email signature -->
  <svg class="email-signature" viewBox="0 0 761 327" xmlns="http://www.w3.org/2000/svg">
    <defs>
      <linearGradient id="gold-sig" x1="0" y1="0" x2="1" y2="1">
        <stop offset="0" stop-color="#b98a3e"/>
        <stop offset="0.5" stop-color="#f3dc8c"/>
        <stop offset="1" stop-color="#c79a4a"/>
      </linearGradient>
    </defs>
    <rect class="signature-base" width="761" height="327" fill="var(--sig-charcoal)"/>
    <circle class="sweep-arc" cx="40" cy="165" r="300" fill="none" stroke="url(#gold-sig)" stroke-width="2.2"/>
    <rect class="info-band" x="215" y="60" width="546" height="212" fill="var(--sig-charcoal)"/>
    <line x1="220" y1="60" x2="761" y2="60" stroke="url(#gold-sig)" stroke-width="1.8"/>
    <line x1="200" y1="272" x2="565" y2="272" stroke="url(#gold-sig)" stroke-width="1.8"/>
    <circle class="orbit-ring" cx="127" cy="170" r="110" fill="var(--sig-charcoal)" stroke="url(#gold-sig)" stroke-width="2"/>
    <circle class="brand-ring" cx="127" cy="170" r="80" fill="none" stroke="url(#gold-sig)" stroke-width="1.8"/>
    <text class="brand-name" x="127" y="166" text-anchor="middle" font-size="14" fill="#d9b866">RIVERLUME</text>
    <text class="brand-name" x="127" y="185" text-anchor="middle" font-size="14" fill="#d9b866">HONEY</text>

    <text x="280" y="103" font-size="29" fill="url(#gold-sig)"><tspan class="name-light">MATTIAS </tspan><tspan class="name-strong">BROVELL</tspan></text>
    <text class="job-title" x="288" y="129" font-size="20" font-weight="600" fill="var(--cream)">Creative Director</text>
    <line x1="275" y1="136" x2="462" y2="136" stroke="url(#gold-sig)" stroke-width="1.2"/>
    <circle cx="462" cy="136" r="3" fill="#d9b866"/>

    <circle cx="273" cy="184" r="12" fill="var(--icon-yellow)" stroke="#f0e3b0" stroke-width="1.2"/>
    <path d="M268.5 179.5c.8-.8 1.8-.8 2.5 0l1.3 1.5c.5.6.4 1.3-.1 1.8l-.8.7c.7 1.3 1.6 2.2 2.9 2.9l.7-.8c.5-.5 1.2-.6 1.8-.1l1.5 1.3c.8.7.8 1.7 0 2.5-2 2-5.3 1-7.8-1.5s-3.4-5.8-2-8.3z" fill="#fff"/>
    <text class="contact-line" x="298" y="192" font-size="23" fill="var(--cream)">+64 2919 58 617</text>

    <circle cx="265" cy="217" r="12" fill="var(--icon-green)" stroke="#f0e3b0" stroke-width="1.2"/>
    <rect x="258.5" y="212.5" width="13" height="9" fill="none" stroke="#fff" stroke-width="1.2"/>
    <path d="M258.5 213l6.5 4.5 6.5-4.5" fill="none" stroke="#fff" stroke-width="1.2"/>
    <text class="contact-line" x="292" y="224" font-size="18" fill="var(--cream)">mattias@riverlumehoney.example</text>

    <circle cx="247" cy="248" r="12" fill="var(--icon-plum)" stroke="#f0e3b0" stroke-width="1.2"/>
    <circle cx="247" cy="248" r="6" fill="none" stroke="#fff" stroke-width="1.1"/>
    <ellipse cx="247" cy="248" rx="2.6" ry="6" fill="none" stroke="#fff" stroke-width="1"/>
    <line x1="241" y1="248" x2="253" y2="248" stroke="#fff" stroke-width="1"/>
    <text class="contact-line" x="280" y="256" font-size="17" fill="var(--cream)">www.riverlumehoney.example</text>

    <text class="social-heading" x="612" y="246" font-size="16" fill="#ffffff">SOCIAL MEDIA:</text>
    <path class="social-pill" d="M578 255H761V290H578a17.5 17.5 0 0 1 0-35z" fill="var(--pill-cream)"/>
    <circle class="social-dot" cx="578" cy="272.5" r="11" fill="var(--social-blue)" stroke="#f0e3b0" stroke-width="1"/>
    <circle class="social-dot" cx="604" cy="272.5" r="11" fill="var(--social-blue)" stroke="#f0e3b0" stroke-width="1"/>
    <text class="social-handle" x="621" y="278" font-size="14" fill="var(--social-blue)">/riverlumehoney/</text>
  </svg>
</main>
</body>
</html>
```